Simple, elegant, business card design required

Hi designers,I am looking for a simple yet elegant business card design.

Please make use of my logo (attached); you are free to tweak the logo should you wish to do so.

Our business is involved in many different fields - almost all of them involved in some form of "design", so that's really one of the key things I want to portray. I do not wish to specify which field of design, exactly.

I prefer white on black (or just monochromatic), but if you have a different, creative idea, I am open to that too.

You can use artsy photographs provided that you have the license to use those. Please feel free to ask me any questions.

Target Market(s)

High-end customers looking for design consultancy

Industry/Entity Type

Business

Contact Information for Business Card

Name: Gareth Pellwinter
Position: Creative Director
Mobile: +150963218745
Address: Morrow Lane, Stratford upon Avon, Warwickshire CV37 2JT
Website: corvastudio.com (not launched yet)

Requirements
Must have
• Design layout must be clean, original, and text must be readable when printed.
Should not have
• ~ No business card templates please. Anyone using this will be reported.
• ~ Please don't spam entries.

```html
<!DOCTYPE html>
<html lang="en">
<head>
<meta charset="UTF-8">
<title>Corva Studio – Business Card</title>
<link rel="stylesheet" href="https://fonts.googleapis.com/css2?family=Vollkorn:wght@400;500&display=swap">
<style>
  :root {
    --ink: #131418;
    --paper: #fbfcfe;
    --white: #ffffff;
  }
  * { margin: 0; padding: 0; box-sizing: border-box; }
  html, body {
    width: 1200px;
    height: 702px;
    overflow: hidden;
    background: var(--paper);
  }
  .card {
    position: relative;
    width: 1200px;
    height: 702px;
    background: var(--paper);
    font-family: "Vollkorn", Georgia, serif;
    font-variant-numeric: lining-nums;
    color: var(--ink);
  }
  .brand-block {
    position: absolute;
    left: 0; top: 0;
    width: 389px; height: 224px;
    background: var(--ink);
  }
  .brand-mark {
    position: absolute;
    left: 286px; top: 84px;
    width: 56px; height: 56px;
    border-radius: 50%;
    background: var(--white);
  }
  .brand-name {
    position: absolute;
    left: 429px; top: 78px;
    font-size: 54px;
    font-weight: 400;
    letter-spacing: 0.06em;
    line-height: 68px;
    color: var(--ink);
    white-space: nowrap;
  }
  .name-band {
    position: absolute;
    left: 0; top: 323px;
    width: 1200px; height: 115px;
    background: var(--ink);
  }
  .person-name {
    position: absolute;
    left: 620px; top: 330px;
    font-size: 52px;
    font-weight: 400;
    line-height: 56px;
    color: var(--white);
    white-space: nowrap;
  }
  .role-tab {
    position: absolute;
    left: 617px; top: 387px;
    width: 583px; height: 51px;
    background: var(--white);
  }
  .person-role {
    position: absolute;
    left: 624px; top: 391px;
    font-size: 33px;
    font-weight: 500;
    line-height: 42px;
    color: var(--ink);
    white-space: nowrap;
  }
  .contact {
    position: absolute;
    left: 64px; top: 482px;
    font-size: 24.5px;
    line-height: 42px;
    font-weight: 500;
  }
  .contact-row {
    display: grid;
    grid-template-columns: 122px 14px auto;
  }
</style>
</head>
<body>
  <div class="card">
    <div class="brand-block">
      <span class="brand-mark"></span>
    </div>
    <div class="brand-name">CORVA STUDIO</div>

    <div class="name-band"></div>
    <div class="person-name">Gareth Pellwinter</div>
    <div class="role-tab"></div>
    <div class="person-role">Creative Director</div>

    <div class="contact">
      <div class="contact-row">
        <span class="contact-label">Mobile</span><span>:</span><span class="contact-value">+150963218745</span>
      </div>
      <div class="contact-row">
        <span class="contact-label">Address</span><span>:</span><span class="contact-value">Morrow Lane, Ashcombe upon Wend,<br>Hollinshire HW12 2JT</span>
      </div>
      <div class="contact-row">
        <span class="contact-label">Website</span><span>:</span><span class="contact-value">corvastudio.com</span>
      </div>
    </div>
  </div>
</body>
</html>
```